Optimization of web page, e-commerce, sell via quillnest and velmorado

I already have my web page in Magento. I just want to improve it, and also sell via Quillnest and Velmorado, I mean, the hole e-commerce. Also Upload images. I have all the photos ready for upload.
I need a page similar to 47tarn.example, because in those page you can buy by quillnest or Velmorado.

I need experience in Magento Website Development, WooCommerce Plugin Development and almost all major PHP Frameworks like

Target Market(s)

Security, soilders, police, camping and sports market

Industry/Entity Type

Security

Number of Pages Required

2 page

Font styles to use
Sans Serif

Colors
85cae6
3176b5
fdf8fb
f9bb94
9d9d9d
cfcfcf
757575
cbcbcb

Requirements
Must have
• The e-commerce, sell via quillnest or velmorado
Nice to have
• Sell via quillnest and Velmorado . Also promotion vía drubbleway
Should not have
• Problems with de the e-commerce

```html
<!DOCTYPE html>
<html lang="en">
<head>
<meta charset="utf-8">
<title>Ridgeline Outfitters – Store</title>
<link href="https://fonts.googleapis.com/css2?family=Roboto:wght@400;500;700&display=swap" rel="stylesheet">
<style>
:root{
  --green:#a8cf3a;
  --red:#e8141b;
  --blue:#3176b5;
  --dark:#333333;
  --ink:#222222;
  --muted:#757575;
  --band:#f4f4f4;
  --soft:#f8f8f8;
  --line:#cfcfcf;
}
*{margin:0;padding:0;box-sizing:border-box}
html,body{width:1200px;height:1200px;overflow:hidden;background:#fff}
body{font-family:'Roboto',Arial,sans-serif;color:var(--ink)}
.stage{position:absolute;left:0;top:0;width:1500px;height:1500px;transform:scale(.8);transform-origin:0 0}
.abs{position:absolute}
.brand{left:478px;top:30px;display:flex;align-items:center;gap:6px;font-size:11px;font-weight:700;color:#555;letter-spacing:.5px;line-height:1.2}
.brand .dot{width:22px;height:22px;border-radius:50%;background:#9d9d9d;flex:none}
.social{display:flex;gap:6px}
.social span{width:12px;height:12px;border-radius:50%;display:block}
.nav{left:727px;top:46px;display:flex;gap:12px;font-size:5.5px;color:#444;text-transform:uppercase;align-items:center}
.photo{background:linear-gradient(135deg,#ececec,#d8d8d8)}
.hero-title{left:797px;top:143px;font-size:30px;font-weight:700;color:var(--green)}
.hero-sub{left:797px;top:187px;font-size:14px;line-height:16px;color:var(--ink)}
.price{font-size:22px;font-weight:700;color:var(--red)}
.btn-outline{border:1px solid var(--green);color:var(--green);font-size:6px;display:flex;align-items:center;justify-content:center}
.btn{background:var(--green);color:#fff;font-size:6px;display:flex;align-items:center;justify-content:center}
.band{left:457px;top:423px;width:587px;height:290px;background:var(--band)}
.card{background:#fff;box-shadow:0 4px 14px rgba(0,0,0,.18)}
.ptitle{font-size:14px;line-height:16px}
.pcopy{font-size:6.5px;line-height:12.3px;color:#555;width:215px}
.news{left:457px;top:947px;width:587px;height:128px;background:var(--blue);color:#fff;text-align:center}
.news h2{font-size:14px;font-weight:400;letter-spacing:3.5px;margin-top:27px}
.news p{font-size:7px;line-height:9px;opacity:.8;margin:10px auto 0;width:250px}
.email{left:177px;top:87px;width:172px;height:17px;background:#fff;color:#777;font-size:6px;text-align:left;padding:5px 7px}
.sub{left:352px;top:87px;width:62px;height:17px;font-weight:700}
.sellers{left:457px;top:1075px;width:587px;height:276px;background:var(--soft)}
.sellers h2{font-size:18px;font-weight:700;text-align:center;margin-top:35px}
.tile{top:78px;width:127px;height:160px;background:#fff;box-shadow:0 1px 4px rgba(0,0,0,.12);text-align:center}
.tile .pic{width:80px;height:70px;margin:12px auto 0;border-radius:4px}
.tile .name{font-size:4.5px;font-weight:700;line-height:7px;margin-top:18px}
.tile .amt{font-size:10px;color:var(--green);margin-top:4px}
.tile .amt s{font-size:6px;color:var(--red);margin-left:5px}
.tile .cart{position:absolute;left:0;bottom:0;width:100%;height:22px;border-top:1px solid #eee;font-size:6px;color:var(--blue);font-weight:500;display:flex;align-items:center;justify-content:center;gap:4px}
.arrow{top:128px;width:22px;height:51px;background:#e8e8e8;display:flex;align-items:center;justify-content:center}
.strip{left:457px;top:1351px;width:587px;height:21px;background:var(--green);display:flex;justify-content:center;align-items:center;gap:20px;color:#fff;font-size:6px;text-transform:uppercase}
.footer{left:457px;top:1372px;width:587px;height:118px;background:var(--dark);color:#ddd}
.col{top:24px;font-size:5.5px;line-height:10px}
.col h4{font-size:7px;font-weight:400;color:var(--green);margin-bottom:5px}
.cards{display:flex;gap:3px;margin-top:4px}
.cards span{width:16px;height:10px;border-radius:1px;display:block}
.copy{left:457px;top:1494px;width:587px;text-align:center;font-size:4.5px;color:#555}
</style>
</head>
<body>
<div class="stage">
  <div class="abs brand"><span class="dot"></span><span>RIDGELINE<br>OUTFITTERS</span></div>
  <div class="abs social" style="left:939px;top:5px">
    <span style="background:#3b5998"></span><span style="background:#cb2027"></span><span style="background:#1da1f2"></span><span style="background:#e4405f"></span>
  </div>
  <nav class="abs nav">
    <span>Home</span><span>Products</span><span>Go shopping</span><span>Ordering info</span><span>About us</span><span>Contact us</span><span>Login</span>
    <svg width="10" height="9" viewBox="0 0 10 9"><path d="M0 1h2l1.5 5h5L10 2.5H3" fill="none" stroke="#444" stroke-width=".9"/><circle cx="4" cy="8" r=".8" fill="#444"/><circle cx="8" cy="8" r=".8" fill="#444"/><circle cx="9" cy="1" r="1.3" fill="#e8141b"/></svg>
    <svg width="8" height="8" viewBox="0 0 8 8"><circle cx="3.2" cy="3.2" r="2.4" fill="none" stroke="#444" stroke-width="1"/><path d="M5 5l2.5 2.5" stroke="#444" stroke-width="1"/></svg>
  </nav>

  <div class="abs photo" role="img" aria-label="Multi function camping cutlery tool with olive green pouch" style="left:483px;top:105px;width:257px;height:255px;background:linear-gradient(135deg,#f4f4f4,#8a8f5a 55%,#e9e9e9)"></div>
  <div class="abs hero-title">NEW ARIVAL</div>
  <div class="abs hero-sub">multi function outdoor tableware<br>stainless camping tool</div>
  <div class="abs price" style="left:797px;top:226px">$ 28.99</div>
  <div class="abs btn-outline" style="left:797px;top:261px;width:62px;height:18px">SHOP NOW</div>

  <div class="abs band"></div>
  <div class="abs card" style="left:740px;top:363px;width:275px;height:252px">
    <div class="photo" role="img" aria-label="Black zoomable tactical LED flashlight with wrist strap" style="margin:30px auto;width:190px;height:190px;background:radial-gradient(circle,#3a3a3a 0,#8a8a8a 45%,#fff 72%)"></div>
  </div>
  <div class="abs ptitle" style="left:513px;top:453px">Lumen K4 Led Flashlight<br>Red Version</div>
  <div class="abs pcopy" style="left:513px;top:494px">Objectively actualize viral outsourcing via premium technology. Uniquely transition diverse niche markets after go forward expertise. Conveniently incubate an expanded array of manufactured products before transparent imperatives.</div>
  <div class="abs price" style="left:511px;top:550px">$ 28.99</div>
  <div class="abs btn" style="left:513px;top:582px;width:62px;height:18px">SHOP NOW</div>

  <div class="abs card" style="left:488px;top:655px;width:276px;height:252px">
    <div class="photo" role="img" aria-label="Silver aluminium flashlight with clip and lanyard" style="margin:28px 0 0 31px;width:211px;height:210px;background:linear-gradient(90deg,#fafafa,#bdbdbd 50%,#fafafa)"></div>
  </div>
  <div class="abs ptitle" style="left:788px;top:736px">Lumen K4 Led Flashlight<br>Red Version</div>
  <div class="abs pcopy" style="left:788px;top:777px">Objectively actualize viral outsourcing via premium technology. Uniquely transition diverse niche markets after go forward expertise. Conveniently incubate an expanded array of manufactured products before transparent imperatives.</div>
  <div class="abs price" style="left:786px;top:832px">$ 28.99</div>
  <div class="abs btn" style="left:788px;top:865px;width:62px;height:18px">SHOP NOW</div>

  <section class="abs news">
    <h2>NEWSLATTER SUBSCRIPTION</h2>
    <p>Phosfluorescently fashion premium processes through front-end ROI. Dynamically reinvent mission-critical intellectual capital for leading</p>
    <div class="abs email">Email</div>
    <div class="abs btn sub">SUBSCRIBE</div>
  </section>

  <section class="abs sellers">
    <h2>TOP SALER</h2>
    <div class="abs arrow" style="left:4px"><svg width="14" height="8" viewBox="0 0 14 8"><path d="M13 4H1M4 1L1 4l3 3" fill="none" stroke="#3176b5" stroke-width="1"/></svg></div>
    <div class="abs arrow" style="left:573px;width:14px"><svg width="10" height="8" viewBox="0 0 10 8"><path d="M0 4h9M6 1l3 3-3 3" fill="none" stroke="#3176b5" stroke-width="1"/></svg></div>
    <div class="abs tile" style="left:36px"><div class="pic photo" role="img" aria-label="Black folding multitool pliers" style="background:linear-gradient(135deg,#fff,#2b2b2b,#fff)"></div><div class="name">11 FUNCTIONS MULTIFUNCTIONAL CAR<br>HERRAMIENTAS PLIERS</div><div class="amt">$ 49.95<s>$ 59.9</s></div><div class="cart"><svg width="8" height="7"><rect x=".5" y="1.5" width="7" height="5" fill="none" stroke="#3176b5"/></svg>ADD TO CART</div></div>
    <div class="abs tile" style="left:169px"><div class="pic photo" role="img" aria-label="Green folding camping spork" style="background:linear-gradient(135deg,#fff,#7cc242,#fff)"></div><div class="name">11 FUNCTIONS MULTIFUNCTIONAL CAR<br>HERRAMIENTAS PLIERS</div><div class="amt">$ 49.95<s>$ 59.9</s></div><div class="cart"><svg width="8" height="7"><rect x=".5" y="1.5" width="7" height="5" fill="none" stroke="#3176b5"/></svg>ADD TO CART</div></div>
    <div class="abs tile" style="left:302px"><div class="pic photo" role="img" aria-label="Red and silver pocket knife" style="background:linear-gradient(135deg,#fff,#d0d0d0,#d9442c,#fff)"></div><div class="name">11 FUNCTIONS MULTIFUNCTIONAL CAR<br>HERRAMIENTAS PLIERS</div><div class="amt">$ 49.95<s>$ 59.9</s></div><div class="cart"><svg width="8" height="7"><rect x=".5" y="1.5" width="7" height="5" fill="none" stroke="#3176b5"/></svg>ADD TO CART</div></div>
    <div class="abs tile" style="left:434px"><div class="pic photo" role="img" aria-label="Black tactical flashlight" style="background:linear-gradient(135deg,#fff,#1f1f1f,#fff)"></div><div class="name">11 FUNCTIONS MULTIFUNCTIONAL CAR<br>HERRAMIENTAS PLIERS</div><div class="amt">$ 49.95<s>$ 59.9</s></div><div class="cart"><svg width="8" height="7"><rect x=".5" y="1.5" width="7" height="5" fill="none" stroke="#3176b5"/></svg>ADD TO CART</div></div>
  </section>

  <div class="abs strip">
    <span>◯&nbsp; International shipping</span><span>•</span><span>◯&nbsp; Customer service</span><span>•</span><span>☎&nbsp; 8:00 A.M. 19:00 P.M.</span>
  </div>

  <footer class="abs footer">
    <div class="abs col" style="left:63px"><h4>Orders and Shipping</h4>Track orders<br>UAE delivery<br>International delivery<br>Refund and returns
      <div class="cards"><span style="background:#f2a23a"></span><span style="background:#ffffff"></span><span style="background:#5fa6d6"></span></div></div>
    <div class="abs col" style="left:218px"><h4>Need help?</h4>Make an appointment<br>Live chat<br>Email support<br>Call us + 555-0142-88</div>
    <div class="abs col" style="left:381px;line-height:8.8px"><h4 style="line-height:10px">Company</h4>About us<br>Products<br>Blog<br>Contact<br>Security Policy<br>Terms of Use</div>
    <div class="abs" style="left:480px;top:28px;display:flex;align-items:center;gap:4px;font-size:6px;font-weight:700;color:#ddd"><span style="width:14px;height:14px;border-radius:50%;background:#9d9d9d;display:block"></span>RIDGELINE</div>
    <div class="abs social" style="left:482px;top:78px;gap:5px">
      <span style="width:9px;height:9px;background:#3b5998"></span><span style="width:9px;height:9px;background:#cb2027"></span><span style="width:9px;height:9px;background:#1da1f2"></span><span style="width:9px;height:9px;background:#e4405f"></span>
    </div>
  </footer>
  <div class="abs copy">© Ridgeline Outfitters 2018. All rights reserved.</div>
</div>
</body>
</html>
```